Brand of baby products for bath & bedding items needs new packaging concept

Our brand is called Cradle Nook and we make products for bath, bedding, maternity body pillows and disposable baby bibs and change mats. We sell to baby stores and retail stores across North America and Europe. Our positioning is mid/high end and we need a new modern look that is simple. We tend to include too much text and overload our packaging. It should be modern and clean. Our current background pattern is a bit too loud and makes things look cluttered. We want a consistent look that can be used across all of our products. It can however have slight differences to categorize the items (ie: all bath items have a particular colour stripe at the bottom to help group them). Please visit out website: www.tinyhavenmarket.example to see more details on the current range and branding. We have products packaged in bags, some in boxes etc... I've also attached our brand presentation. The final design should communicate quality and comfort.

Target Market(s)

Baby products that appeal to moms and dads

Industry/Entity Type

Baby

Colors
876aae
85acd3
5c5c5c
9d9d9d
33b8a4
b768aa
87cfc6

Requirements
Should not have
• It should not be gender specific. It needs to include colours that appeal to both boys and girls. Blue is OK but pink is not. I also don't like yellow or orange. I like "soft" and light colours.

```html
<!DOCTYPE html>
<html lang="en">
<head>
<meta charset="utf-8">
<title>Cradle Nook – Bamboo Hands Free Hoodie packaging</title>
<link href="https://fonts.googleapis.com/css2?family=Open+Sans:wght@400;600&display=swap" rel="stylesheet">
<style>
  :root {
    --stage: #1c1c1e;
    --pack-blue: #22bde0;
    --pack-band: #2ec6e6;
    --pack-wave: #3cc8e8;
    --spine-blue: #2bb7d5;
    --spine-inner: #29b3d2;
    --logo-fill: #9fe1ee;
    --logo-edge: #5a9fb5;
    --accent-purple: #876aae;
    --ink-white: #ffffff;
    --ink-brand: #3f86c4;
    --photo-light: #eef1f3;
    --photo-mid: #c9b8a6;
    --cloud-soft: #63d3ee;
  }
  * { box-sizing: border-box; margin: 0; padding: 0; }
  html, body { width: 1200px; height: 800px; overflow: hidden; }
  body {
    background: var(--stage);
    font-family: "Open Sans", Arial, sans-serif;
    position: relative;
  }

  /* Dieline panels */
  .panel {
    position: absolute;
    top: 111px;
    width: 366px;
    height: 539px;
    background: var(--pack-blue);
    overflow: hidden;
  }
  .panel--front { left: 88px; }
  .panel--back { left: 755px; }

  .panel__wave {
    position: absolute;
    inset: 0;
    width: 366px;
    height: 539px;
  }

  .face {
    position: absolute;
    left: 0;
    width: 366px;
  }
  .face--upper { top: 0; height: 232px; }
  .face--lower { top: 284px; height: 229px; transform: rotate(180deg); }

  .brand-tag {
    position: absolute;
    background: var(--ink-white);
    border: 1px solid #8a8fa0;
    border-radius: 3px;
    display: flex;
    align-items: center;
    justify-content: center;
    color: var(--accent-purple);
    font-weight: 600;
    white-space: nowrap;
  }
  .face .brand-tag {
    left: 25px; top: 22px;
    width: 61px; height: 30px;
    font-size: 9px;
  }

  .product-title {
    position: absolute;
    left: 26px; top: 94px;
    color: var(--ink-white);
    font-weight: 600;
    font-size: 10px;
  }
  .feature-list {
    position: absolute;
    left: 30px; top: 111px;
    list-style: none;
    color: var(--ink-white);
    font-size: 4.6px;
    line-height: 9.2px;
  }
  .feature-list li::before { content: "• "; }

  .size-tag {
    position: absolute;
    left: 17px; top: 208px;
    width: 79px; height: 15px;
    background: var(--accent-purple);
    color: var(--ink-white);
    font-size: 4.4px;
    line-height: 4.6px;
    text-align: center;
    padding-top: 1px;
  }

  .lettering-spot {
    position: absolute;
    left: 172px; top: 30px;
    width: 60px; height: 38px;
    border-radius: 18px;
    background: var(--cloud-soft);
    opacity: .7;
  }

  .hero-photo {
    position: absolute;
    left: 0; top: 0;
    width: 366px; height: 232px;
  }

  .name-band {
    position: absolute;
    left: 0; top: 232px;
    width: 366px; height: 52px;
    background: var(--pack-band);
  }
  .name-band .brand-tag {
    left: 24px; top: 2px;
    width: 52px; height: 26px;
    font-size: 8px;
  }
  .name-band__title {
    position: absolute;
    left: 105px; top: 4px;
    color: var(--ink-white);
    font-size: 14px;
    letter-spacing: 1.2px;
  }

  /* Spine / gusset */
  .spine {
    position: absolute;
    left: 478px; top: 0;
    width: 254px; height: 800px;
    background: var(--spine-blue);
  }
  .spine__inner {
    position: absolute;
    left: 24px; top: 0;
    width: 206px; height: 800px;
    background: var(--spine-inner);
    box-shadow: 3px 0 6px rgba(0,0,0,.18), -2px 0 4px rgba(0,0,0,.08);
  }
  .spine__brand {
    position: absolute;
    left: 54px; top: 324px;
    width: 147px; height: 74px;
    background: var(--logo-fill);
    border: 2px solid var(--logo-edge);
    border-radius: 6px;
    display: flex;
    align-items: center;
    justify-content: center;
    color: var(--ink-brand);
    font-weight: 600;
    font-size: 20px;
  }
</style>
</head>
<body>

  <!-- Front panel -->
  <section class="panel panel--front">
    <svg class="panel__wave" viewBox="0 0 366 539" aria-hidden="true">
      <path d="M0 150 Q180 90 366 70 L366 232 L0 232 Z" fill="var(--pack-wave)" opacity=".35"/>
      <path d="M0 430 Q180 470 366 460 L366 539 L0 539 Z" fill="var(--pack-wave)" opacity=".3"/>
    </svg>

    <div class="face face--upper">
      <svg class="hero-photo" viewBox="0 0 366 232" role="img" aria-label="Photo of a smiling baby crawling under a white hooded towel">
        <defs>
          <linearGradient id="photoToneA" x1="0" y1="0" x2="1" y2="1">
            <stop offset="0" stop-color="var(--photo-light)"/>
            <stop offset="1" stop-color="var(--photo-mid)"/>
          </linearGradient>
        </defs>
        <path d="M174 232 Q198 62 350 17 L350 232 Z" fill="url(#photoToneA)"/>
        <path d="M174 232 Q198 62 350 17" fill="none" stroke="var(--accent-purple)" stroke-width="3"/>
      </svg>
      <div class="brand-tag">Cradle Nook</div>
      <div class="lettering-spot" role="img" aria-label="Hand lettered softness badge"></div>
      <h2 class="product-title">Hooded Apron Towel</h2>
      <ul class="feature-list">
        <li>Premium &amp; luxurious comfort &amp; absorbency</li>
        <li>Extra large hooded towel perfect for toddlers too</li>
        <li>Unique apron design features pull-over neck hole &amp; GripTab</li>
        <li>fastens around parents' backs to make "hands free"</li>
        <li>Soft &amp; cozy rayon from bamboo &amp; organic cotton terry</li>
      </ul>
      <div class="size-tag">Perfect for toddlers too!<br>100x100 CM<br>39,4"x 39,4"</div>
    </div>

    <div class="name-band">
      <div class="brand-tag">Cradle Nook</div>
      <p class="name-band__title">Bamboo Hands Free Hoodie</p>
    </div>

    <div class="face face--lower">
      <svg class="hero-photo" viewBox="0 0 366 232" role="img" aria-label="Photo of a baby wrapped in a white hooded towel">
        <defs>
          <linearGradient id="photoToneB" x1="0" y1="0" x2="1" y2="1">
            <stop offset="0" stop-color="var(--photo-light)"/>
            <stop offset="1" stop-color="var(--photo-mid)"/>
          </linearGradient>
        </defs>
        <path d="M174 232 Q198 62 350 17 L350 232 Z" fill="url(#photoToneB)"/>
        <path d="M174 232 Q198 62 350 17" fill="none" stroke="var(--accent-purple)" stroke-width="3"/>
      </svg>
      <div class="brand-tag">Cradle Nook</div>
      <div class="lettering-spot" role="img" aria-label="Hand lettered softness badge"></div>
      <h2 class="product-title">Hooded Apron Towel</h2>
      <ul class="feature-list">
        <li>Premium &amp; luxurious comfort &amp; absorbency</li>
        <li>Extra large hooded towel perfect for toddlers too</li>
        <li>Unique apron design features pull-over neck hole &amp; GripTab</li>
        <li>fastens around parents' backs to make "hands free"</li>
        <li>Soft &amp; cozy rayon from bamboo &amp; organic cotton terry</li>
      </ul>
      <div class="size-tag">Perfect for toddlers too!<br>100x100 CM<br>39,4"x 39,4"</div>
    </div>
  </section>

  <!-- Spine -->
  <section class="spine">
    <div class="spine__inner"></div>
    <div class="spine__brand">Cradle Nook</div>
  </section>

  <!-- Back panel -->
  <section class="panel panel--back">
    <svg class="panel__wave" viewBox="0 0 366 539" aria-hidden="true">
      <path d="M0 150 Q180 90 366 70 L366 232 L0 232 Z" fill="var(--pack-wave)" opacity=".35"/>
      <path d="M0 430 Q180 470 366 460 L366 539 L0 539 Z" fill="var(--pack-wave)" opacity=".3"/>
    </svg>

    <div class="face face--upper">
      <div class="brand-tag">Cradle Nook</div>
      <div class="lettering-spot" role="img" aria-label="Hand lettered softness badge"></div>
      <h2 class="product-title">Hooded Apron Towel</h2>
      <ul class="feature-list">
        <li>Premium &amp; luxurious comfort &amp; absorbency</li>
        <li>Extra large hooded towel perfect for toddlers too</li>
        <li>Unique apron design features pull-over neck hole &amp; GripTab</li>
        <li>fastens around parents' backs to make "hands free"</li>
        <li>Soft &amp; cozy rayon from bamboo &amp; organic cotton terry</li>
      </ul>
      <div class="size-tag">Perfect for toddlers too!<br>100x100 CM<br>39,4"x 39,4"</div>
    </div>

    <div class="name-band">
      <div class="brand-tag">Cradle Nook</div>
      <p class="name-band__title">Bamboo Hands Free Hoodie</p>
    </div>

    <div class="face face--lower">
      <div class="brand-tag">Cradle Nook</div>
      <div class="lettering-spot" role="img" aria-label="Hand lettered softness badge"></div>
      <h2 class="product-title">Hooded Apron Towel</h2>
      <ul class="feature-list">
        <li>Premium &amp; luxurious comfort &amp; absorbency</li>
        <li>Extra large hooded towel perfect for toddlers too</li>
        <li>Unique apron design features pull-over neck hole &amp; GripTab</li>
        <li>fastens around parents' backs to make "hands free"</li>
        <li>Soft &amp; cozy rayon from bamboo &amp; organic cotton terry</li>
      </ul>
      <div class="size-tag">Perfect for toddlers too!<br>100x100 CM<br>39,4"x 39,4"</div>
    </div>
  </section>

</body>
</html>
```